Pagina Lartécnica

The Lartécnica is a company dealing with leasing and selling real estate. The current site can be accessed at www.lartecnica-exemplo.com.br. We intend to redesign the look of the site and for that we would like to redesign the home page and the page with information and pictures of the property. The homepage should maintain the characteristics of the current common design simple, short and straightforward. The page with the data of the properties should be accessed with two changes page as it is currently running. The search from the map by region and should be maintained.
The page containing the information of the property will provide a total of 15 small pictures that when clicked will appear in larger size. The colors to be used should be orange, blue, black and white. The map can be maintained in the current colors.
Updates

Project Deadline Extended
Reason: Payment guarante!!

Payment guaranteed. Deadline for submission of designs April 27.

Industry/Entity Type

Real Estate

Requirements
Must have
• Search by map regions and search box
address
keep colors from the current page
phones
clean look
Nice to have
• clean look
Should not have
• We like the current page. We just want to make it compatible with modern and new design trends and monitors.

```html
<!DOCTYPE html>
<html lang="en">
<head>
<meta charset="utf-8">
<title>Lartécnica – Home</title>
<link href="https://fonts.googleapis.com/css2?family=Roboto+Condensed:wght@300;400;700&family=Arimo:wght@400&display=swap" rel="stylesheet">
<style>
:root{
  --purple:#524a6e;
  --purple-dark:#2f2a52;
  --orange:#f0801e;
  --text:#7a7a7a;
  --side:#f2efe9;
  --line:#b7b3c8;
  --foot-muted:#a7a2bd;
}
*{margin:0;padding:0;box-sizing:border-box}
html,body{width:1200px;height:938px;overflow:hidden;background:#fff}
.stage{width:1280px;height:1000px;transform:scale(.9375);transform-origin:0 0;position:relative;font-family:"Roboto Condensed",sans-serif}
.site{position:absolute;left:158px;top:0;width:980px}
.top-bar{height:10px;background:var(--purple)}
.header{height:173px;position:relative;border-bottom:1px solid var(--line)}
.header::after{content:"";position:absolute;left:0;right:0;bottom:-4px;border-bottom:1px solid var(--line)}
.brand{position:absolute;left:32px;top:58px;display:flex;align-items:center;gap:12px}
.brand-mark{width:22px;height:22px;background:var(--orange)}
.brand-name{font-size:46px;font-weight:700;color:var(--purple);letter-spacing:-.5px}
.nav{position:absolute;left:560px;top:22px;display:grid;grid-template-columns:205px 215px;row-gap:10px}
.nav a{display:flex;align-items:center;gap:9px;height:25px;font-size:21px;font-weight:300;color:var(--orange);text-decoration:none;letter-spacing:-.6px;white-space:nowrap}
.nav svg{width:9px;height:11px;flex:none}
.main{display:flex;height:650px;margin-top:3px}
.content{width:666px;padding:30px 10px 0 30px;position:relative}
.welcome{display:inline-block;font-size:36px;font-weight:700;letter-spacing:-.5px;padding-bottom:2px;border-bottom:1px dotted #999;line-height:1}
.welcome .hl{color:var(--orange)}
.welcome .name{color:var(--purple)}
.content p{font-family:"Arimo",sans-serif;font-size:14.4px;line-height:20px;color:var(--text);margin-top:20px}
.content p:first-of-type{margin-top:6px}
.content-rule{position:absolute;left:50px;right:30px;top:550px;height:2px;background:linear-gradient(90deg,transparent,var(--line),transparent)}
.sidebar{width:314px;background:var(--side);border-left:1px dotted #aaa;padding:30px 0 0 31px;position:relative}
.side-title{font-size:27px;font-weight:300;color:var(--purple-dark);letter-spacing:-.6px;line-height:30px;padding-bottom:3px;border-bottom:1px dotted #999;display:inline-block}
.checks{margin:12px 0 0 122px;width:76px}
.check{display:flex;justify-content:space-between;align-items:center;font-size:16px;font-weight:300;color:var(--purple-dark);height:29px}
.check span.box{width:8px;height:8px;border:1px solid #888;background:#fff;border-radius:1px}
.field{margin:6px 0 0 97px;width:101px;height:31px;background:#fff;border:1px solid #bbb;border-radius:3px;display:flex;align-items:center;justify-content:space-between;padding:0 6px;font-size:16px;font-weight:300;color:var(--purple-dark)}
.field+.field{margin-top:9px}
.drop{width:14px;height:14px;background:var(--orange);border-radius:2px;display:flex;align-items:center;justify-content:center}
.side-sep{margin:20px 0 0 10px;width:220px;border-top:1px dotted #bbb}
.region{margin-top:17px;width:238px}
.map{position:absolute;left:88px;top:338px;width:182px;height:280px;background:linear-gradient(160deg,#e9efc8 0%,#8fc8e8 35%,#e8b27c 55%,#7fbfe6 75%,#d9e8f0 100%);border:2px solid #fff;box-shadow:3px 3px 5px rgba(0,0,0,.3)}
.footer{height:114px;background:var(--purple);position:relative;color:#fff}
.address{position:absolute;left:30px;top:9px;font-size:14px;line-height:17px;font-style:normal}
.foot-brand{position:absolute;right:28px;top:38px;font-size:26px;font-weight:700;color:var(--foot-muted)}
.copy{position:absolute;left:0;right:0;top:90px;text-align:center;font-size:11.5px;color:var(--foot-muted)}
</style>
</head>
<body>
<div class="stage">
<div class="site">
  <div class="top-bar"></div>
  <header class="header">
    <div class="brand"><span class="brand-mark"></span><span class="brand-name">Lartécnica</span></div>
    <nav class="nav">
      <a href="#"><svg viewBox="0 0 9 11"><path d="M1 1l6 4.5L1 10" fill="none" stroke="#3c3658" stroke-width="2.2"/></svg>The company</a>
      <a href="#"><svg viewBox="0 0 9 11"><path d="M1 1l6 4.5L1 10" fill="none" stroke="#3c3658" stroke-width="2.2"/></svg>List your property</a>
      <a href="#"><svg viewBox="0 0 9 11"><path d="M1 1l6 4.5L1 10" fill="none" stroke="#3c3658" stroke-width="2.2"/></svg>Location</a>
      <a href="#"><svg viewBox="0 0 9 11"><path d="M1 1l6 4.5L1 10" fill="none" stroke="#3c3658" stroke-width="2.2"/></svg>Owner Info</a>
      <a href="#"><svg viewBox="0 0 9 11"><path d="M1 1l6 4.5L1 10" fill="none" stroke="#3c3658" stroke-width="2.2"/></svg>Restricted Area</a>
      <a href="#"><svg viewBox="0 0 9 11"><path d="M1 1l6 4.5L1 10" fill="none" stroke="#3c3658" stroke-width="2.2"/></svg>Information for Tenant</a>
      <a href="#"><svg viewBox="0 0 9 11"><path d="M1 1l6 4.5L1 10" fill="none" stroke="#3c3658" stroke-width="2.2"/></svg>Contact Us</a>
      <a href="#"><svg viewBox="0 0 9 11"><path d="M1 1l6 4.5L1 10" fill="none" stroke="#3c3658" stroke-width="2.2"/></svg>Request your property</a>
    </nav>
  </header>
  <div class="main">
    <section class="content">
      <h1 class="welcome"><span class="hl">Welcome to</span> <span class="name">LARTÉCNICA</span></h1>
      <p>The Lartécnica, for over fifteen years in the real estate market, permeated the culture and values defined by the needs of its customers, is gradually building a solid body for the management and sale of real estate. Theseyears marked by moments of achievement and adversity, brought him the wisdom necessary to build step by step a large gap in the provision of its services.</p>
      <p>Bring happiness to relationships, provide solidity to the continuing purpose of serving, has been objectively the character of their actions.</p>
      <p>Movements in search of a personalized service have the convenience of the Customer, its greater purpose. Has been its commitment to sustain permanently ethical management, fully honoring all financial commitments</p>
      <p>tax, making transparent the relationship with clients, be they owners, tenants, sellers or buyers.</p>
      <p>The Lartécnica is a company in constant search for innovation, skilled professionals, using the best information technology and sensitivity to lead the administration of the property of its customers ensuring a policy of absolute respect.</p>
      <p>Supported these principles, happiness, convenience, empowerment, innovation, technology, hard work and a lot of creativity, Lartécnica is always in search of new horizons relying on the valuable support of clients and friends.</p>
      <div class="content-rule"></div>
    </section>
    <aside class="sidebar">
      <h2 class="side-title">Search for properties</h2>
      <div class="checks">
        <label class="check"><span class="box"></span>To Buy</label>
        <label class="check"><span class="box"></span>Rent</label>
      </div>
      <div class="field">Every<span class="drop"><svg width="8" height="6" viewBox="0 0 8 6"><path d="M1 1l3 3 3-3" fill="none" stroke="#fff" stroke-width="1.6"/></svg></span></div>
      <div class="field">Buscar<svg width="26" height="24" viewBox="0 0 26 24"><line x1="1" y1="6" x2="1" y2="18" stroke="#ccc"/><circle cx="13" cy="10" r="6" fill="none" stroke="#f0801e" stroke-width="2.5"/><line x1="17" y1="14" x2="23" y2="21" stroke="#f0801e" stroke-width="3.5" stroke-linecap="round"/></svg></div>
      <div class="side-sep"></div>
      <h2 class="side-title region">Search property by region (location)</h2>
      <div class="map" role="img" aria-label="Regional map of the island and mainland districts, clickable by region"></div>
    </aside>
  </div>
  <footer class="footer">
    <address class="address">Rua das Acácias, 140 - Street Corner with Rua do Porto - Centro -<br>CEP: 88000-100 - Fax: (48) 3000-0000</address>
    <div class="foot-brand">Lartécnica</div>
    <div class="copy">(C) 2013 - Lartécnica - All rights reserved.</div>
  </footer>
</div>
</div>
</body>
</html>
```